Fall Postcard Mailers for Roofing Company

We need a postcard for a mailer designed for ShingleGuide. ShingleGuide is professional and personable. Unlike most roofing companies our Advisors are Non-Commissioned so they provide Unbiased advise. Our Advisors provide an In-depth Roof Analysis for each home. This is much like a home inspection report with pictures and description.

Homeowner demographics are upscale neighborhoods with homeowners over 40 years old with properties over $250,000. All pictures and colors can be pulled from www.ShingleGuideMi.example and our Facebook page https://www.facebook.com/MyShingleGuide/. We are based in Plymouth, Mi.

I've attached some of our other marketing materials.

Target Market(s)

Homeowners
40 years old and above
Home value over $250,000

Industry/Entity Type

Roofing

Requirements
Must have
• Space designed for mail printing on front
• Add a three discount coupons
• -Up to $2,500 off Roof Replacement
• -FREE Roof Analysis up to $500 value
• -Up to $100 off Roof Repair
• Non-Commissioned Advisors=Unbiased Guidance
• Financing Available
• Company colors:
• G: C-0 M-0 Y-0 K-80
• O: C-0 M-54 Y-95 K-0
Nice to have
• We are trying to drive action: Calls, website visits, inquiries.
• Personable and professional.
Should not have
• Too much open space.

```html
<!DOCTYPE html>
<html lang="en">
<head>
<meta charset="utf-8">
<title>ShingleGuide Fall Postcard Mailer</title>
<link rel="stylesheet" href="https://fonts.googleapis.com/css2?family=Open+Sans:wght@300;400;600;700;800&family=Oswald:wght@400;500;600&family=Dancing+Script:wght@600&display=swap">
<style>
  :root {
    --brand-grey: #575757;
    --brand-grey-dark: #3f3f3f;
    --brand-orange: #f58a1f;
    --sky: #cfe0ee;
    --brick: #b8643f;
    --shingle: #6e4a3e;
    --white: #ffffff;
    --stage: #2e2e2e;
    --ink: #4a4a4a;
  }
  * { box-sizing: border-box; margin: 0; padding: 0; }
  html, body { width: 960px; height: 1200px; overflow: hidden; }
  body { background: var(--stage); font-family: "Open Sans", Arial, sans-serif; position: relative; }
  h1, h2, h3 { font-weight: 400; }

  .postcard { position: absolute; overflow: hidden; background: var(--white); }

  /* ---------- Front ---------- */
  .postcard--front { left: 128px; top: 50px; width: 705px; height: 541px; }
  .hero-photo {
    position: absolute; inset: 0;
    background: linear-gradient(170deg, var(--sky) 0%, #e3ecf3 30%, #c98a63 52%, var(--brick) 70%, #7a4a36 100%);
  }
  .roof-frame { position: absolute; left: 0; top: 0; }
  .brand-name {
    position: absolute; font-family: "Open Sans", Arial, sans-serif;
    font-weight: 600; color: var(--brand-orange); white-space: nowrap; letter-spacing: -0.5px;
  }
  .postcard--front .brand-name { right: 58px; top: 28px; font-size: 48px; line-height: 56px; }

  .age-badge {
    position: absolute; left: 30px; top: 36px; width: 144px; height: 144px; border-radius: 50%;
    background: radial-gradient(circle at 50% 30%, #8a8a8a 0%, #5d5d5d 55%, #444 100%);
    border: 4px solid #e8e8e8; color: var(--white); text-align: center;
    font-family: "Oswald", "Arial Narrow", sans-serif; font-weight: 500;
    box-shadow: 0 2px 6px rgba(0,0,0,.35);
  }
  .age-badge__over { position: absolute; top: 14px; left: 0; right: 0; font-size: 15px; line-height: 18px; margin-left: -28px; }
  .age-badge__years { position: absolute; top: 28px; left: 22px; display: flex; align-items: center; }
  .age-badge__num { font-size: 46px; line-height: 48px; font-weight: 600; }
  .age-badge__unit { font-size: 15px; line-height: 16px; text-align: left; margin-left: 4px; }
  .age-badge__props { position: absolute; top: 78px; left: 0; right: 0; font-size: 12.5px; line-height: 14px; }
  .age-badge__value { position: absolute; top: 92px; left: 0; right: 0; font-size: 27px; line-height: 32px; font-weight: 600; }

  .headline { position: absolute; left: 386px; top: 166px; font-family: "Open Sans", Arial, sans-serif; font-weight: 400; }
  .headline__line { display: block; font-size: 42px; line-height: 46px; color: var(--brand-grey-dark); letter-spacing: 1px; font-weight: 400; }
  .headline__line--accent { color: var(--brand-orange); font-weight: 700; }

  .message-band {
    position: absolute; left: 0; right: 0; top: 396px; bottom: 0;
    background: rgba(45,42,40,.86); color: var(--white); text-align: center;
  }
  .message-band__lead { margin-top: 16px; font-size: 21.5px; font-weight: 800; letter-spacing: .3px; line-height: 26px; }
  .message-band__sub { font-size: 19.5px; font-weight: 400; letter-spacing: .3px; line-height: 26px; }
  .call-button { position: absolute; left: 110px; top: 81px; width: 470px; height: 50px; }
  .call-button__text {
    position: absolute; inset: 0; display: flex; align-items: center; justify-content: center;
    font-size: 17px; letter-spacing: .3px; gap: 6px; padding-right: 10px;
  }
  .call-button__script { font-family: "Dancing Script", cursive; font-size: 23px; }
  .call-button__phone { font-weight: 700; }

  /* ---------- Back ---------- */
  .postcard--back { left: 131px; top: 618px; width: 705px; height: 542px; }
  .offer-panel { position: absolute; left: 0; top: 0; width: 353px; height: 542px; background: var(--white); }
  .offer-photo {
    position: absolute; left: 0; top: 40px; width: 353px; height: 250px;
    background: linear-gradient(160deg, var(--sky) 0%, #dfe8ef 28%, #8c6a5c 50%, var(--shingle) 75%, #5a3c33 100%);
  }
  .offer-title {
    position: absolute; right: 23px; top: 22px; color: var(--white);
    font-size: 29px; line-height: 36px; letter-spacing: .5px; font-weight: 400;
  }
  .offer-title strong { font-weight: 700; }

  .coupons { position: absolute; left: 17px; top: 262px; display: flex; gap: 13px; }
  .coupon {
    width: 99px; height: 96px; padding: 4px; background: var(--brand-orange);
    border: 2px solid #6d6d6d; box-shadow: 0 3px 4px rgba(0,0,0,.35);
  }
  .coupon--grey { background: var(--brand-grey); border-color: var(--brand-orange); }
  .coupon__inner {
    height: 100%; border: 1.5px dashed rgba(255,255,255,.85); color: var(--white);
    padding: 6px 0 0 5px; font-family: "Oswald", "Arial Narrow", sans-serif; overflow: hidden;
  }
  .coupon__upto { font-size: 21px; line-height: 24px; font-weight: 500; }
  .coupon__amount { display: flex; align-items: center; font-size: 25px; line-height: 28px; font-weight: 500; white-space: nowrap; }
  .coupon__off { writing-mode: vertical-rl; transform: rotate(180deg); font-size: 9px; line-height: 10px; margin-right: 2px; }
  .coupon__value { font-size: 11px; margin-left: 2px; align-self: flex-end; line-height: 20px; }
  .coupon__label { font-family: "Open Sans", Arial, sans-serif; font-size: 8px; line-height: 14px; white-space: nowrap; letter-spacing: -0.2px; margin-top: 2px; }
  .coupon__label strong { font-weight: 700; }

  .promise { position: absolute; left: 0; width: 353px; text-align: center; color: var(--ink); }
  .promise--unbiased { top: 372px; font-size: 13px; }
  .promise--financing { top: 393px; font-size: 19px; }

  .contact-block { position: absolute; left: 0; top: 427px; width: 353px; height: 93px; background: var(--brand-orange); color: var(--white); padding: 10px 8px 0 20px; }
  .contact-block__title { font-size: 17px; line-height: 22px; letter-spacing: .3px; padding-bottom: 3px; border-bottom: 1.5px solid rgba(255,255,255,.9); width: 312px; font-weight: 400; }
  .contact-row { display: flex; align-items: center; gap: 4px; font-size: 14px; line-height: 22px; white-space: nowrap; }
  .contact-row--first { margin-top: 5px; }
  .contact-row__web { font-size: 12.5px; letter-spacing: -0.2px; margin-left: 8px; display: flex; align-items: center; gap: 3px; }
  .contact-row small { font-size: 13.5px; }

  .follow-bar { position: absolute; left: 0; top: 520px; width: 353px; height: 22px; background: var(--brand-grey); color: var(--white); display: flex; justify-content: flex-end; align-items: center; gap: 5px; padding-right: 16px; font-size: 11px; font-weight: 600; letter-spacing: .3px; }
  .follow-bar__dot { width: 14px; height: 14px; border-radius: 50%; background: var(--white); }

  .mail-side { position: absolute; left: 353px; top: 0; width: 352px; height: 542px; background: var(--white); }
  .postcard--back .brand-name { left: 48px; top: 48px; font-size: 28px; line-height: 36px; }
  .stamp-box { position: absolute; left: 242px; top: 18px; width: 91px; height: 91px; background: #dcdcdc; }
</style>
</head>
<body>

<section class="postcard postcard--front" aria-label="Postcard front">
  <div class="hero-photo" role="img" aria-label="Photo of roofers laying brown shingles on a brick house under construction"></div>
  <svg class="roof-frame" width="705" height="160" viewBox="0 0 705 160" aria-hidden="true">
    <polyline points="0,142 182,22 344,134 705,134" fill="none" stroke="var(--brand-orange)" stroke-width="24" stroke-linejoin="miter"/>
    <polyline points="0,133 182,13 336,119 705,119" fill="none" stroke="var(--white)" stroke-width="3"/>
    <polygon points="0,0 705,0 705,114 336,114 182,8 0,128" fill="var(--brand-grey)"/>
  </svg>
  <div class="brand-name">ShingleGuide</div>

  <div class="age-badge">
    <span class="age-badge__over">OVER</span>
    <div class="age-badge__years">
      <span class="age-badge__num">40</span>
      <span class="age-badge__unit">YEARS<br>OLD WITH</span>
    </div>
    <span class="age-badge__props">PROPERTIES OVER</span>
    <span class="age-badge__value">$250,000</span>
  </div>

  <h1 class="headline">
    <span class="headline__line">LET US MEET</span>
    <span class="headline__line headline__line--accent">YOUR ROOF</span>
  </h1>

  <div class="message-band">
    <p class="message-band__lead">WE START WITH AN IN-DEPTH ANALYSIS, NOT A SALES PITCH</p>
    <p class="message-band__sub">PROFESSIONAL ADVICE TAILORED TO YOUR ROOFING NEEDS</p>
    <div class="call-button">
      <svg width="470" height="50" viewBox="0 0 470 50" aria-hidden="true">
        <rect x="2" y="2" width="460" height="40" rx="8" fill="none" stroke="var(--white)" stroke-width="1.3" transform="rotate(-0.6 235 25)"/>
        <rect x="8" y="7" width="458" height="40" rx="8" fill="none" stroke="var(--white)" stroke-width="1.3" transform="rotate(0.5 235 25)"/>
      </svg>
      <div class="call-button__text">
        <span>SPEAK WITH A ROOFING</span>
        <span class="call-button__script">Expert</span>
        <span class="call-button__phone">877-555-0142</span>
      </div>
    </div>
  </div>
</section>

<section class="postcard postcard--back" aria-label="Postcard back">
  <div class="offer-panel">
    <div class="offer-photo" role="img" aria-label="Photo of roofers working on a shingled roof beside a chimney"></div>
    <svg class="roof-frame" width="353" height="90" viewBox="0 0 353 90" aria-hidden="true">
      <polyline points="0,76 90,32 166,80 353,80" fill="none" stroke="var(--brand-orange)" stroke-width="16"/>
      <polyline points="0,67 90,23 162,71 353,71" fill="none" stroke="var(--white)" stroke-width="2.5"/>
      <polygon points="0,0 353,0 353,66 158,66 90,18 0,62" fill="var(--brand-grey)"/>
    </svg>
    <h2 class="offer-title">OUR <strong>OFFER</strong></h2>

    <div class="coupons">
      <div class="coupon">
        <div class="coupon__inner">
          <div class="coupon__upto">UP TO</div>
          <div class="coupon__amount"><span class="coupon__off">OFF</span>$2,500</div>
          <div class="coupon__label">Roof Replacement</div>
        </div>
      </div>
      <div class="coupon coupon--grey">
        <div class="coupon__inner">
          <div class="coupon__upto">UP TO</div>
          <div class="coupon__amount">$500<span class="coupon__value">VALUE</span></div>
          <div class="coupon__label"><strong>FREE</strong> Roof Analysis</div>
        </div>
      </div>
      <div class="coupon">
        <div class="coupon__inner">
          <div class="coupon__upto">UP TO</div>
          <div class="coupon__amount"><span class="coupon__off">OFF</span>$100</div>
          <div class="coupon__label">Roof Repair</div>
        </div>
      </div>
    </div>

    <p class="promise promise--unbiased">Non-Commissioned Advisors=Unbiased Guidance</p>
    <p class="promise promise--financing">Financing Available</p>

    <div class="contact-block">
      <h3 class="contact-block__title">CONTACT US</h3>
      <div class="contact-row contact-row--first">
        <svg width="10" height="10" viewBox="0 0 10 10" aria-hidden="true"><path d="M1 3 Q5 0 9 3 L8 4.5 L6.5 4 L6.5 3.3 Q5 2.8 3.5 3.3 L3.5 4 L2 4.5 Z M2 5.5 H8 L8.5 9 H1.5 Z" fill="#ffffff"/></svg>
        <span>(734) 555-0187</span>
        <span class="contact-row__web">
          <svg width="10" height="10" viewBox="0 0 10 10" aria-hidden="true"><circle cx="5" cy="5" r="4.2" fill="none" stroke="#ffffff" stroke-width="1"/><ellipse cx="5" cy="5" rx="1.8" ry="4.2" fill="none" stroke="#ffffff" stroke-width=".8"/><line x1=".8" y1="5" x2="9.2" y2="5" stroke="#ffffff" stroke-width=".8"/></svg>
          www.ShingleGuideMi.example
        </span>
      </div>
      <div class="contact-row">
        <svg width="10" height="13" viewBox="0 0 10 13" aria-hidden="true"><path d="M5 0.5 A4.2 4.2 0 0 1 9.2 4.7 C9.2 7.5 5 12.5 5 12.5 C5 12.5 0.8 7.5 0.8 4.7 A4.2 4.2 0 0 1 5 0.5 Z M5 3 A1.6 1.6 0 1 0 5 6.2 A1.6 1.6 0 1 0 5 3 Z" fill="#ffffff" fill-rule="evenodd"/></svg>
        <small>4820 Maple Ridge Rd. Plymouth, MI 48170</small>
      </div>
    </div>
    <div class="follow-bar">
      <span>FOLLOW US ON</span>
      <span class="follow-bar__dot"></span>
      <span class="follow-bar__dot"></span>
    </div>
  </div>

  <div class="mail-side">
    <div class="brand-name">ShingleGuide</div>
    <div class="stamp-box" aria-label="Postage area"></div>
  </div>
</section>

</body>
</html>
```